Professional "Aviation Parts" Auction Website with Customer Login Backend Module

Need an "Aviation Parts" Website with 4 major listing options.
- AUCTION
Seller can list their items on the site as an auction with a small listing fee. Seller has to create an account in order to be able to create or edit a listing. Seller must be able to have a reserve price.
- SELLING
Sellers can list their items with a small listing fee. Imortant is, that Sellers has a back end module, (like trovix) where they can log in and create or make changes to existing listings.
- BUYING
Buyers can search items either by part number in a search bar, or scroll through categories and subcategories to find the respective part.
- WANTED
Customers should be able to create a “Wanted” listing for items of interest.

In all four cases, customers (Buyers/Seller) must create an account to either place a bid, buy now, create a “wanted” listing or create/edit their own for sale/auction listing. NO login is required to search the website or browse through categories and to see listings. The website should be “Trovix like” with login module, payment, coindrop connection, etc and easy to navigate. A design example is https://www.quellmarket-hub.com/ . I’m open for all ideas.

Target Market(s)

Aviation Industry
Helicopter Industry

Industry/Entity Type

Aviation

Number of Pages Required

5+ page

Font styles to use
Serif
Sans Serif

Colors
85acd3
3176b5
9d9d9d
d3d3d3

Requirements
Must have
• Our company is called Brelvox.com, LLC and is specialized in aviation parts listings. The website must have 4 major options: Auction, Sell, Buy, and Wanted listings. The Buyer/Seller must create an account in order to bid, buy or sell an item. No login is required if someone just wants to browse the website to look for pricing and parts. Once they decide to purchase, they have to login or create an account. The same counts for the seller. Seller must create an account to list a "For Sale", "Auction" or "Wanted" Listing. Each listing requires a small listing fee, which will be charged by us and should be paid via CoinDrop. CoinDrop should be interfaced as a preferred payment method. Other payment options are available as well. The website idea is very similar to Trovix. Same style listings as Trovix and other auction pages. A good design idea is https://www.quellmarket-hub.com/ to get a better understanding. The website must be easy to navigate and modern looking with a professional color scheme. The logo is attached. I would like to keep the website in a similar color scheme as the logo design.
• There should be two main Categories on the main page to select from:
• - Helicopter Listings
• - Airplane Listings
• The 1st "Sub-Category" once you click on either one of the top category, will be "Aircraft Make".
• The 2nd "Sub-Category" will be "Aircraft Model".
• The 3rd "Sub-Category" will be "Parts" for that specific aircraft.
• Also there should be a CoinDrop interface, if a buyer wants to purchase an item, so they can use their credit card or request wire information from the seller after closing.
• It also has to include an option when a seller lists an item, they will be required to make a payment to us for listing on our website. For example $1.99 for a listing value up to $100. A listing fee for a sale value of up to $1,000 will be $4.99, and so on. Listing fee for up to $10,000 will be $14.99. Listing fee for up to $100.000 will be $49.99. This system is very similar to the Trovix platform.
Nice to have
• It would be nice to have a easy to maintain back-end module which can easily be manged by our personnel.
Should not have
• The page should not look childish with random colors. A professional appearance and easy to navigate is a must.

```html
<!DOCTYPE html>
<html lang="en">
<head>
<meta charset="utf-8">
<title>Brelvox – Aviation Parts</title>
<link rel="stylesheet" href="https://fonts.googleapis.com/css2?family=Roboto:wght@400;500;700&family=Montserrat:wght@400;500;600&family=Nunito:wght@800&family=Open+Sans:wght@400;600&display=swap">
<style>
:root{
  --blue:#2a5ea8;
  --blue-light:#85acd3;
  --blue-mid:#3176b5;
  --ink:#1a1a1a;
  --grey:#9d9d9d;
  --grey-light:#d3d3d3;
  --dark:#1e1e1e;
  --footer:#171717;
  --bottom:#0d0d0d;
  --white:#ffffff;
}
*{margin:0;padding:0;box-sizing:border-box}
html,body{width:1200px;height:2225px;overflow:hidden;background:var(--white);font-family:"Montserrat",sans-serif;color:var(--ink)}
.page{position:relative;width:1200px;height:2225px}
.abs{position:absolute}

/* header */
.site-header{position:absolute;left:0;top:0;width:1200px;height:122px;background:var(--white)}
.brand{position:absolute;left:133px;top:12px;width:182px;text-align:center}
.brand-mark{display:block;margin:0 auto 4px;width:72px;height:72px;border-radius:50%;border:4px solid var(--blue)}
.brand-name{font-family:"Roboto",sans-serif;font-weight:500;font-size:24px;letter-spacing:2px;color:var(--blue-mid)}
.topbar{position:absolute;left:410px;top:0;width:680px;height:36px;background:var(--dark);clip-path:polygon(0 0,100% 0,96% 100%,4% 100%);display:flex;align-items:center;font-family:"Roboto",sans-serif;font-size:13px;color:#eee}
.topbar .call{display:flex;align-items:center;gap:10px;margin-left:40px;font-size:14px}
.topbar .signup{display:flex;align-items:center;gap:8px;margin-left:auto;padding:0 18px;height:36px;border-left:1px solid #444}
.topbar .signup:first-of-type{margin-left:auto}
.topbar .search{display:flex;align-items:center;height:36px;padding:0 40px 0 22px;border-left:1px solid #444}
.topbar .links{display:flex;margin-left:auto}
.main-nav{position:absolute;top:72px;left:439px;display:flex;gap:33px;font-family:"Roboto",sans-serif;font-size:16px;font-weight:500;color:var(--ink)}

/* hero */
.hero{position:absolute;left:0;top:122px;width:1200px;height:505px;background:radial-gradient(ellipse at 45% 30%,#5a5e62 0%,#3a3d41 45%,#25272a 100%)}
.hero-title{position:absolute;left:0;top:140px;width:1200px;text-align:center;font-family:"Roboto",sans-serif;font-weight:700;font-size:56px;color:var(--white);letter-spacing:1px}
.cat-tab{position:absolute;top:244px;height:39px;width:140px;font-family:"Roboto",sans-serif;font-weight:500;font-size:15px;color:var(--white);display:flex;align-items:center;justify-content:center}
.cat-tab.active{left:454px;background:var(--blue)}
.cat-tab.off{left:606px;background:var(--blue-light)}
.finder{position:absolute;left:211px;top:283px;width:779px;height:69px;background:var(--blue);display:flex;align-items:center;padding:0 10px;gap:8px}
.select{width:207px;height:35px;background:var(--white);font-family:"Roboto",sans-serif;font-size:12px;color:#333;display:flex;align-items:center;justify-content:space-between;padding:0 12px 0 16px}
.select i{width:0;height:0;border-left:4px solid transparent;border-right:4px solid transparent;border-top:5px solid #333}
.finder-btn{margin-left:4px;width:104px;height:35px;background:#1b1b1b;color:var(--white);font-family:"Roboto",sans-serif;font-weight:500;font-size:14px;display:flex;align-items:center;justify-content:center}
.dots{position:absolute;top:393px;left:560px;display:flex;gap:8px;align-items:center}
.dots span{width:12px;height:12px;border-radius:50%;background:var(--white)}
.dots span.on{width:20px;height:20px;background:transparent;border:2px solid var(--white);position:relative}
.dots span.on::after{content:"";position:absolute;left:3px;top:3px;width:10px;height:10px;border-radius:50%;background:var(--white)}

/* listings */
.list-tabs{position:absolute;top:707px;left:306px;display:flex;gap:20px}
.pill{height:36px;border:2px solid var(--blue);border-radius:18px;font-family:"Roboto",sans-serif;font-weight:500;font-size:19px;color:var(--blue);display:flex;align-items:center;justify-content:center}
.pill.on{background:var(--blue);color:var(--white)}
.card{position:absolute;top:793px;width:216px}
.card .photo{width:216px;height:195px;border:1px solid #cfcfcf;padding:4px;background:var(--white)}
.card .photo div{width:100%;height:100%;background:radial-gradient(circle at 50% 50%,#5a5d63 0%,#9a9ca0 38%,#eeeeee 60%)}
.card h3{margin-top:20px;font-weight:500;font-size:16px;color:var(--ink)}
.card p{margin-top:10px;font-size:12px;line-height:21px;color:#222}
.card .price{margin-top:13px;font-size:16px;font-weight:500;color:var(--blue-mid)}
.card .actions{margin-top:12px;display:flex;gap:10px}
.btn{height:29px;border-radius:15px;font-size:13px;display:flex;align-items:center;justify-content:center;border:2px solid #333;color:#222}
.btn.buy{width:96px}
.btn.bid{width:96px;border-color:var(--blue-mid);color:var(--blue-mid)}
.arrow{position:absolute;top:912px;width:25px;height:25px;border-radius:50%;border:1px solid #444;display:flex;align-items:center;justify-content:center}

/* newsletter */
.newsletter{position:absolute;left:0;top:1284px;width:1200px;height:444px;background:linear-gradient(180deg,#2c3036 0%,#3b3f45 50%,#262829 100%)}
.news-box{position:absolute;left:300px;top:113px;width:600px;height:226px;border:3px solid #d9d9d9;border-radius:6px;background:rgba(0,0,0,.25)}
.news-title{position:absolute;top:82px;width:100%;text-align:center;font-family:"Nunito",sans-serif;font-weight:800;font-size:32px;color:var(--white);letter-spacing:.5px}
.news-form{position:absolute;left:40px;top:138px;width:520px;height:53px;display:flex}
.news-form .field{flex:1;background:var(--white);border-radius:27px 0 0 27px;font-family:"Open Sans",sans-serif;font-size:11px;color:#999;display:flex;align-items:center;padding-left:24px}
.news-form .go{width:122px;background:var(--blue);border-radius:0 27px 27px 0;color:var(--white);font-family:"Roboto",sans-serif;font-weight:500;font-size:15px;display:flex;align-items:center;justify-content:center}

/* footer */
.site-footer{position:absolute;left:0;top:1728px;width:1200px;height:387px;background:var(--footer);color:var(--white)}
.foot-brand{position:absolute;left:134px;top:94px;width:160px;text-align:center}
.foot-brand .brand-mark{width:60px;height:60px;border:3px solid var(--white);margin-bottom:6px}
.foot-brand .brand-name{color:var(--white);font-size:19px}
.social{display:flex;gap:4px;justify-content:center;margin-top:12px}
.social span{width:24px;height:24px;border-radius:50%;border:1px solid var(--white)}
.foot-h{position:absolute;font-family:"Roboto",sans-serif;font-weight:500;font-size:19px}
.foot-h::after{content:"";position:absolute;left:4px;top:36px;width:96px;height:2px;background:linear-gradient(90deg,var(--blue-light) 0 40%,var(--white) 40%)}
.contact-row{position:absolute;left:350px;display:flex;gap:14px;font-family:"Open Sans",sans-serif;font-size:13px;line-height:18px;letter-spacing:.3px}
.post{position:absolute;left:585px;display:flex;gap:18px}
.post .thumb{width:84px;height:64px;border:2px solid #ddd;background:linear-gradient(135deg,#4b6c8e,#9aa6b2 60%,#c98a5a)}
.post h4{font-family:"Open Sans",sans-serif;font-weight:600;font-size:14px;line-height:21px;width:230px}
.post .date{margin-top:6px;font-family:"Open Sans",sans-serif;font-size:12px;display:flex;gap:8px;align-items:center}
.quick{position:absolute;left:951px;top:137px;list-style:none;font-family:"Open Sans",sans-serif;font-size:12px;line-height:24px}
.bottom-bar{position:absolute;left:0;top:2115px;width:1200px;height:110px;background:var(--bottom);color:var(--white);font-family:"Open Sans",sans-serif;font-size:12px;text-align:center;padding-top:54px}
</style>
</head>
<body>
<div class="page">

<header class="site-header">
  <div class="brand"><span class="brand-mark"></span><span class="brand-name">BRELVOX</span></div>
  <div class="topbar">
    <span class="call">
      <svg width="16" height="16" viewBox="0 0 24 24"><path fill="#fff" d="M6.6 10.8a15 15 0 0 0 6.6 6.6l2.2-2.2a1 1 0 0 1 1-.25 11 11 0 0 0 3.6.6 1 1 0 0 1 1 1V20a1 1 0 0 1-1 1A17 17 0 0 1 3 4a1 1 0 0 1 1-1h3.5a1 1 0 0 1 1 1c0 1.25.2 2.45.6 3.6a1 1 0 0 1-.25 1z"/></svg>
      Call Us 800-555-0147!
    </span>
    <span class="links">
      <span class="signup">SIGNUP BUYER
        <svg width="10" height="12" viewBox="0 0 10 12"><rect x="1" y="5" width="8" height="7" fill="#fff"/><path d="M3 5V3.5a2 2 0 0 1 4 0V5" stroke="#fff" stroke-width="1.4" fill="none"/></svg></span>
      <span class="signup">SIGNUP SELLER
        <svg width="10" height="12" viewBox="0 0 10 12"><circle cx="5" cy="3" r="2.6" fill="#fff"/><path d="M0 12a5 5 0 0 1 10 0z" fill="#fff"/></svg></span>
      <span class="search"><svg width="14" height="14" viewBox="0 0 14 14"><circle cx="6" cy="6" r="4.3" stroke="#fff" stroke-width="2" fill="none"/><path d="M9 9l4 4" stroke="#fff" stroke-width="2.2"/></svg></span>
    </span>
  </div>
  <nav class="main-nav"><span>HOME</span><span>AUCTION</span><span>SELLING</span><span>BUYING</span><span>ABOUT US</span><span>WANTED</span><span>CONTACT</span></nav>
</header>

<section class="hero" role="img" aria-label="Close-up photo of an aircraft propeller engine under cloudy sky">
  <h1 class="hero-title">AVIATION PARTS</h1>
  <div class="cat-tab active">HELICOPTER</div>
  <div class="cat-tab off">AIRPLANE</div>
  <div class="finder">
    <div class="select">Aircraft Make <i></i></div>
    <div class="select">Aircraft Model <i></i></div>
    <div class="select">Parts <i></i></div>
    <div class="finder-btn">SEARCH</div>
  </div>
  <div class="dots"><span class="on"></span><span></span><span></span><span></span></div>
</section>

<div class="list-tabs">
  <div class="pill on" style="width:132px">AUCTION</div>
  <div class="pill" style="width:132px">SELLING</div>
  <div class="pill" style="width:132px">BUYING</div>
  <div class="pill" style="width:132px">WANTED</div>
</div>

<div class="arrow" style="left:86px"><svg width="8" height="10" viewBox="0 0 8 10"><path d="M6 1L2 5l4 4" stroke="#333" stroke-width="1.5" fill="none"/></svg></div>
<div class="arrow" style="left:1086px"><svg width="8" height="10" viewBox="0 0 8 10"><path d="M2 1l4 4-4 4" stroke="#333" stroke-width="1.5" fill="none"/></svg></div>

<article class="card" style="left:131px">
  <div class="photo"><div role="img" aria-label="Photo of a turbofan engine with blue fan blades"></div></div>
  <h3>Nemo enim ipsam</h3>
  <p>Sed ut perspiciatis unde omnis iste natus error sit voluptatem accustium doloremque laudantium</p>
  <div class="price">$49.99</div>
  <div class="actions"><span class="btn buy">Buy Now</span><span class="btn bid">Bid Now</span></div>
</article>
<article class="card" style="left:371px">
  <div class="photo"><div role="img" aria-label="Photo of a radial engine with a three-blade propeller"></div></div>
  <h3>Nemo enim ipsam</h3>
  <p>Sed ut perspiciatis unde omnis iste natus error sit voluptatem accustium doloremque laudantium</p>
  <div class="price">$49.99</div>
  <div class="actions"><span class="btn buy">Buy Now</span><span class="btn bid">Bid Now</span></div>
</article>
<article class="card" style="left:611px">
  <div class="photo"><div role="img" aria-label="Photo of a jet engine exhaust section"></div></div>
  <h3>Nemo enim ipsam</h3>
  <p>Sed ut perspiciatis unde omnis iste natus error sit voluptatem accustium doloremque laudantium</p>
  <div class="price">$49.99</div>
  <div class="actions"><span class="btn buy">Buy Now</span><span class="btn bid">Bid Now</span></div>
</article>
<article class="card" style="left:851px">
  <div class="photo"><div role="img" aria-label="Photo of an open turbofan engine cutaway"></div></div>
  <h3>Nemo enim ipsam</h3>
  <p>Sed ut perspiciatis unde omnis iste natus error sit voluptatem accustium doloremque laudantium</p>
  <div class="price">$49.99</div>
  <div class="actions"><span class="btn buy">Buy Now</span><span class="btn bid">Bid Now</span></div>
</article>

<section class="newsletter" role="img" aria-label="Photo of an airliner parked inside a maintenance hangar">
  <div class="news-box">
    <svg class="abs" style="left:277px;top:26px" width="46" height="40" viewBox="0 0 46 40"><g fill="none" stroke="#fff" stroke-width="2.2" stroke-linejoin="round"><path d="M4 18L24 4l18 14-20 16z"/><path d="M4 18l18 16"/><path d="M10 22l14-8"/></g></svg>
    <h2 class="news-title">NEWSLETTER SIGN UP</h2>
    <div class="news-form"><div class="field">Enter your email address</div><div class="go">SUBSCRIBE</div></div>
  </div>
</section>

<footer class="site-footer">
  <div class="foot-brand">
    <span class="brand-mark"></span><span class="brand-name">BRELVOX</span>
    <div class="social" aria-label="Social links"><span></span><span></span><span></span><span></span></div>
  </div>

  <h3 class="foot-h" style="left:350px;top:73px">CONTACT US</h3>
  <div class="contact-row" style="top:145px">
    <svg width="14" height="18" viewBox="0 0 14 18"><path d="M7 17S1 10.5 1 6.5a6 6 0 0 1 12 0C13 10.5 7 17 7 17z" fill="none" stroke="#fff" stroke-width="1.3"/><circle cx="7" cy="6.5" r="2" fill="none" stroke="#fff" stroke-width="1.3"/></svg>
    <span>Aviation Parts<br>Lindqvistgatan 8<br>114 22 Norrvik</span>
  </div>
  <div class="contact-row" style="top:210px">
    <svg width="16" height="16" viewBox="0 0 24 24"><path fill="none" stroke="#fff" stroke-width="1.6" d="M6.6 10.8a15 15 0 0 0 6.6 6.6l2.2-2.2a1 1 0 0 1 1-.25 11 11 0 0 0 3.6.6 1 1 0 0 1 1 1V20a1 1 0 0 1-1 1A17 17 0 0 1 3 4a1 1 0 0 1 1-1h3.5a1 1 0 0 1 1 1c0 1.25.2 2.45.6 3.6a1 1 0 0 1-.25 1z"/></svg>
    <span>Phone: 08-555 019</span>
  </div>
  <div class="contact-row" style="top:242px">
    <svg width="18" height="14" viewBox="0 0 18 14"><rect x="1" y="1" width="16" height="12" fill="none" stroke="#fff" stroke-width="1.3"/><path d="M1 1l8 7 8-7" fill="none" stroke="#fff" stroke-width="1.3"/></svg>
    <span>info@brelvox.com</span>
  </div>

  <h3 class="foot-h" style="left:585px;top:74px">BLOG FEED</h3>
  <div class="post" style="top:144px">
    <div class="thumb" role="img" aria-label="Photo of a technician working on aircraft equipment"></div>
    <div><h4>Nemo enim ipsam voluptatem sit aspernatur aut odit</h4>
      <div class="date"><svg width="11" height="11" viewBox="0 0 11 11"><rect x="0" y="1.5" width="11" height="9.5" fill="#fff"/><rect x="1.5" y="4" width="8" height="5.5" fill="#171717"/></svg>JULY 05, 2018</div></div>
  </div>
  <div class="post" style="top:232px">
    <div class="thumb" role="img" aria-label="Photo of an engineer in a hard hat near an aircraft"></div>
    <div><h4>Nemo enim ipsam voluptatem sit aspernatur aut odit</h4>
      <div class="date"><svg width="11" height="11" viewBox="0 0 11 11"><rect x="0" y="1.5" width="11" height="9.5" fill="#fff"/><rect x="1.5" y="4" width="8" height="5.5" fill="#171717"/></svg>JULY 05, 2018</div></div>
  </div>

  <h3 class="foot-h" style="left:951px;top:70px">QUICK LINKS</h3>
  <ul class="quick"><li>Home</li><li>Auction</li><li>Selling</li><li>Buying</li><li>About Us</li><li>Wanted</li><li>Contact</li></ul>
</footer>

<div class="bottom-bar">Copyright © Aviation Parts 2018. All rights reserved.</div>

</div>
</body>
</html>
```